female stress management consultant, doctor, Health & Well-being coach needs a wordpress theme

I am a Stress management consultant, General Practitioner and Health and Well-Being coach who is targeting mainly surgeries/hospitals and corporate business.
I have my own URL drhelgabrunsvik.com and the hosting.
I need a WordPress Website that is easy to maintain and edit to regularly change the content (copy/pictures/action buttons/banners).
I want my website to look professional and elegant for corporate businesses and managers to feel they can trust me and my expertise. At the same time, the website should have a warm and welcoming feel to it. It should feel uplifting and very positive.
I am open to colour suggestions, but please incorporate the following two colours: #F18877 and #D2BB7A. For fonts I prefer grey over black (like #777777).
The website needs to create an impression of "know like and trust".
The website should have a sign-up button for a newsletter, multiple contact buttons over the home page - to write an email to me, contact details top and bottom and the possibility to have a video on the home page top instead of a picture (Best would be that I can change from picture to video to picture in the future without needing a designer). A video that can run in the background with text laid over. A bit like on this website from Tessa Vanrijn: https://www.tessavanrijn.com.
I need 5 pages: Home, About, Services, Contact, free resources. I do NOT need an e-commerce or booking facility as I will neither sell nor let people book through my website. I don't need a blog either.
All the pages need to have a link to my other website (brightpathdaily.co.uk) and it needs to state that the linked website (brightpathdaily) is my website with a blog and for private customers.
Please use the photos I attached if possible. Me with the dogs for the "about" section.

Websites I like: https://www.olgabkr.com, tessavanrijn.com, https://ruthpembly.com (this site is too dark for my liking, but the layout has a simple navigation layout, the important buttons are right up at the side (WorkLattice/social media/CTA), is minimalistic - hence easy to find the important bits).

Target Market(s)

surgeries/doctor offices, hospitals, corporate business

Industry/Entity Type

Health and well-being

Coding

Coded - Design and coding required

Number of Pages Required

5+ page

Font styles to use
Sans Serif

Requirements
Must have
• see project description
Nice to have
• see project description

```html
<!DOCTYPE html>
<html lang="en">
<head>
<meta charset="utf-8">
<title>Contact – Dr Helga Brunsvik</title>
<link rel="stylesheet" href="https://fonts.googleapis.com/css2?family=Oswald:wght@300;400;600&family=Poppins:wght@400;500;600&display=swap">
<style>
:root{
  --coral:#F18877;
  --coral-deep:#ec7a68;
  --gold:#D2BB7A;
  --grey:#777777;
  --grey-dark:#555555;
  --ink:#333333;
  --white:#ffffff;
  --line:#9a9a9a;
}
*{box-sizing:border-box;margin:0;padding:0}
html,body{width:1200px;height:1200px;overflow:hidden;background:var(--white)}
body{position:relative;font-family:'Poppins',sans-serif;color:var(--grey)}
.page{position:absolute;left:297.5px;top:67.5px;width:574px;height:1108px}
.abs{position:absolute}

/* top contact bar */
.topbar{left:0;top:0;width:574px;height:19px;background:var(--coral);color:var(--white);font-size:8.2px}
.topbar .item{position:absolute;display:flex;align-items:center;gap:5px;top:0;height:19px}
.topbar .divider{position:absolute;left:148px;top:5px;width:1px;height:10px;background:rgba(255,255,255,.7)}
.social-top{position:absolute;right:58px;top:0;height:19px;display:flex;align-items:center;gap:6px;font-size:5.5px}

/* header */
.brand{left:18px;top:22px;width:90px;text-align:center}
.brand .mark{display:block;width:9px;height:9px;border-radius:50%;background:var(--gold);margin:12px auto 5px}
.brand .name{font-size:7.4px;color:var(--coral);white-space:nowrap}
.brand .tag{font-size:3.4px;color:var(--coral);white-space:nowrap;letter-spacing:.2px}
.nav{left:162.5px;top:42px;width:230px;height:12px;font-size:8px;color:var(--grey-dark)}
.nav a{position:absolute;top:0;text-decoration:none;color:inherit;white-space:nowrap;line-height:12px}
.nav a.current{color:var(--coral)}
.cta{left:444.5px;top:37.5px;width:96.5px;height:20px;background:var(--coral);color:var(--white);font-size:7.3px;border-radius:2px;display:flex;align-items:center;justify-content:center}

/* hero */
.hero{left:0;top:76.5px;width:574px;height:252px;background:linear-gradient(180deg,#2b3520 0%,#1e2619 45%,#3c4a2f 100%)}
.hero-copy{left:51.5px;top:155px;width:480px;color:var(--white)}
.hero-copy .eyebrow{display:flex;align-items:center;gap:8px;font-size:7.5px;font-weight:600;line-height:10px}
.hero-copy .eyebrow .rule{width:17px;height:1px;background:var(--coral)}
.hero-copy h1{font-family:'Oswald',sans-serif;font-weight:600;font-size:25px;line-height:29px;margin-top:5px;letter-spacing:.1px}
.hero-copy p{font-size:7.9px;margin-top:6px;font-weight:500;white-space:nowrap}

/* photo panels */
.sky{left:0;top:328.5px;width:286.5px;height:251.5px;background:linear-gradient(180deg,#8a9099 0%,#a9b2c0 55%,#c4ccd6 100%)}
.portrait{left:286.5px;top:493.5px;width:287.5px;height:396px;background:linear-gradient(160deg,#6f8a45 0%,#556d36 45%,#7d8a70 75%,#9a8466 100%)}

/* help block */
.help{left:355.5px;top:345px}
.help h2{font-family:'Oswald',sans-serif;font-weight:300;color:var(--coral);font-size:20.5px;line-height:20px}
.contact-col{font-size:8px}
.contact-col .label{color:var(--grey-dark);font-weight:500}
.contact-col .label.condensed{font-family:'Oswald',sans-serif;font-weight:400;font-size:8.5px}
.contact-col .value{color:var(--grey);margin-top:4px}

/* form */
.form{left:34.5px;top:606px;width:160px}
.field label{display:block;font-size:7.4px;color:var(--grey-dark);line-height:9px}
.field .box{width:159px;height:17px;border:1px solid var(--line);border-radius:1px;margin-bottom:11.5px}
.field .box.area{width:156px;height:108px}
.submit{width:52.5px;height:19px;background:var(--coral);color:var(--white);font-size:7.5px;font-weight:600;border-radius:5px;display:flex;align-items:center;justify-content:center}

/* footer */
.foot-brand{left:51px;top:930px;width:90px;text-align:center}
.foot-brand .mark{display:block;width:12px;height:12px;border-radius:50%;background:var(--gold);margin:14px auto 12px}
.foot-brand .name{font-size:9.4px;color:var(--coral);white-space:nowrap}
.foot-brand .tag{font-size:4px;color:var(--coral);letter-spacing:.4px;white-space:nowrap;margin-top:1px}
.foot-title{font-family:'Oswald',sans-serif;font-weight:400;color:var(--coral);font-size:11px}
.foot-link{font-size:6px;color:var(--grey-dark)}
.subscribe-text{font-size:6.2px;line-height:11px;color:var(--grey-dark);text-transform:uppercase}
.subscribe{left:385px;top:975px;width:135px;height:21.5px;border:1px solid var(--coral);border-radius:11px;overflow:hidden;display:flex;align-items:center}
.subscribe span{font-size:5.6px;color:var(--grey-dark);margin-left:8.5px;flex:1}
.subscribe .send{width:17px;height:21.5px;background:var(--coral);display:flex;align-items:center;justify-content:center}
.social-foot{left:51px;top:1026px;display:flex;gap:10px;font-size:5.5px;color:var(--grey-dark);align-items:center}
.social-foot span{display:flex;align-items:center;gap:3px}
.social-foot i{display:block;width:7px;height:7px;border-radius:50%;border:1px solid #d9d9d9}

.bottombar{left:0;top:1073.5px;width:574px;height:34px;background:var(--coral);color:var(--white);font-size:6.6px;font-weight:600}
.bottombar .copy{position:absolute;left:51.5px;top:11px}
.bottombar .links a{position:absolute;top:13px;color:var(--white);text-decoration:none;font-size:6.2px;font-weight:500}
</style>
</head>
<body>
<div class="page">

  <div class="abs topbar">
    <div class="item" style="left:53px">
      <svg width="10" height="10" viewBox="0 0 24 24" fill="none" stroke="#fff" stroke-width="1.8"><path d="M5 3h4l2 5-2.5 1.5a11 11 0 0 0 6 6L16 13l5 2v4a2 2 0 0 1-2 2A16 16 0 0 1 3 5a2 2 0 0 1 2-2z"/></svg>
      <span>+1 (212)-555-0148</span>
    </div>
    <div class="divider"></div>
    <div class="item" style="left:153px">
      <svg width="11" height="10" viewBox="0 0 24 20" fill="none" stroke="#fff" stroke-width="1.8"><rect x="2" y="3" width="20" height="15" rx="1"/><path d="M2 4l10 8 10-8"/></svg>
      <span>info@drhelgabrunsvik.com</span>
    </div>
    <div class="social-top">
      <span>Kinly</span><span>Pipit</span><span>WorkLattice</span><span>Dotfield</span><span>Snapwell</span>
    </div>
  </div>

  <div class="abs brand">
    <span class="mark"></span>
    <div class="name">Dr Helga Brunsvik</div>
    <div class="tag">Create a life you love living</div>
  </div>

  <nav class="abs nav">
    <a style="left:0" href="#">Home</a>
    <a style="left:35px" href="#">About</a>
    <a style="left:70px" href="#">Services</a>
    <a style="left:114px" class="current" href="#">Contact</a>
    <a style="left:157.5px" href="#">Free Resources</a>
  </nav>
  <div class="abs cta">BRIGHTPATHDAILY</div>

  <section class="abs hero" role="img" aria-label="Photo of a woman laughing with arms outstretched in a meadow of wildflowers"></section>
  <div class="abs hero-copy">
    <div class="eyebrow"><span class="rule"></span>CONTACT</div>
    <h1>write an email at:<br>info@drhelgabrunsvik.com</h1>
    <p>If you have a question or want to get in touch with me, please use this contact form</p>
  </div>

  <div class="abs sky" role="img" aria-label="Photo of a rainbow across a grey cloudy sky"></div>

  <div class="abs help"><h2>HOW CAN<br>WE HELP YOU?</h2></div>
  <div class="abs contact-col" style="left:344.5px;top:418px">
    <div class="label condensed">Phone</div>
    <div class="value">(212) 555-0172</div>
  </div>
  <div class="abs contact-col" style="left:442.5px;top:417px">
    <div class="label">Email</div>
    <div class="value">info@drhelgabrunsvik.com</div>
  </div>

  <div class="abs portrait" role="img" aria-label="Photo of the coach kneeling on grass with her two dogs"></div>

  <form class="abs form">
    <div class="field"><label>Your name</label><div class="box"></div></div>
    <div class="field"><label>Your email</label><div class="box"></div></div>
    <div class="field"><label>Subject</label><div class="box"></div></div>
    <div class="field"><label>Your message (optional)</label><div class="box area"></div></div>
    <div class="submit">Submit</div>
  </form>

  <div class="abs foot-brand">
    <span class="mark"></span>
    <div class="name">Dr Helga Brunsvik</div>
    <div class="tag">Create a life you love living</div>
  </div>

  <div class="abs foot-title" style="left:219.5px;top:927px">Useful Links</div>
  <div class="abs foot-link" style="left:222.5px;top:954px">About Me</div>
  <div class="abs foot-link" style="left:222.5px;top:971px">Services</div>
  <div class="abs foot-link" style="left:301.5px;top:954px">Contact Us</div>
  <div class="abs foot-link" style="left:301.5px;top:971px">Free Resources</div>

  <div class="abs foot-title" style="left:385px;top:927px">Subscribe Now</div>
  <div class="abs subscribe-text" style="left:385px;top:947px">Get regular inspiration for health,<br>wellbeing and happiness</div>
  <div class="abs subscribe">
    <span>Your mail here</span>
    <div class="send"><svg width="9" height="8" viewBox="0 0 24 20" fill="none" stroke="#fff" stroke-width="2"><rect x="2" y="3" width="20" height="15" rx="1"/><path d="M2 4l10 8 10-8"/></svg></div>
  </div>

  <div class="abs social-foot">
    <span><i></i>Kinly</span><span><i></i>Pipit</span><span><i></i>WorkLattice</span><span><i></i>Dotfield</span><span><i></i>Snapwell</span>
  </div>

  <footer class="abs bottombar">
    <div class="copy">©2023. Dr Helga Brunsvik. All Rights Reserved.</div>
    <div class="links">
      <a style="left:395.5px" href="#">Home</a>
      <a style="left:422.5px" href="#">Contact Us</a>
      <a style="left:463.5px" href="#">Bright Path Daily</a>
    </div>
  </footer>

</div>
</body>
</html>
```